KFO R Training Website

We need a website to post videos, blogs and other information or links.
We teach Jujitsu , combatives, Metaphysical Coaching. I want to tach online and in person. Silver Heron Institute Deals in several areas of Personal Protection and Coaching.
Training (Martial Arts / combative)
Emotional Intelligence
Leadership Development
Motivation
Our Log is attached.
Similar Websites to what we do ( we want to stand out better).
https://marcovelden.example/
https://raybusko.example/
https://summitfusionmentoring.example/
Industry/Entity Type
Training , Martial Arts, coaching
Coding
Coded - Design and coding required
Number of Pages Required
2 page
Look and feel

```html
<!DOCTYPE html>
<html lang="en">
<head>
<meta charset="utf-8">
<title>Silver Heron Institute — KFO R Training</title>
<link href="https://fonts.googleapis.com/css2?family=Archivo:wght@700;800;900&family=Montserrat:wght@400;500;600;700&display=swap" rel="stylesheet">
<style>
:root{
  --red:#e4222a;
  --red-deep:#b51d22;
  --black:#0b0b0b;
  --panel:#1c1c1c;
  --card:#222222;
  --white:#ffffff;
  --muted:#cfcfcf;
  --grey:#8a8a8a;
}
*{margin:0;padding:0;box-sizing:border-box}
html,body{width:1200px;height:4843px;overflow:hidden;background:var(--black)}
body{position:relative;font-family:"Montserrat",sans-serif;color:var(--white)}
.abs{position:absolute}
.heading{font-family:"Archivo",sans-serif;font-weight:800;letter-spacing:.5px;text-transform:uppercase;color:var(--red);font-size:40px;line-height:1}
.band{position:absolute;left:0;width:1200px}

/* header / hero */
.hero{top:0;height:703px;background:radial-gradient(ellipse 520px 560px at 930px 330px,#5a5a5a 0%,#2d2d2d 45%,#121212 80%),#111}
.hero-photo{position:absolute;right:0;top:0;width:600px;height:703px;background:radial-gradient(ellipse 260px 330px at 380px 330px,rgba(120,120,120,.55),rgba(0,0,0,0) 70%)}
.logo{position:absolute;left:141px;top:28px;width:94px;height:79px;background:var(--white);border-radius:8px;display:flex;flex-direction:column;align-items:center;justify-content:center;gap:6px}
.logo-mark{width:22px;height:22px;border-radius:50%;background:var(--black)}
.logo-name{font-size:7px;font-weight:700;color:var(--black);text-align:center;line-height:1.2;width:80px}
.nav{position:absolute;top:53px;left:577px;font-size:15px;font-weight:500}
.nav a{color:var(--white);text-decoration:none;position:absolute;white-space:nowrap}
.hero-rule{position:absolute;left:118px;top:179px;width:2px;height:385px;background:var(--red)}
.hero-title{position:absolute;left:141px;top:172px;font-family:"Archivo",sans-serif;font-weight:800;font-size:68px;line-height:103px;color:var(--white);white-space:nowrap}
.hero-title span{color:var(--red)}
.hero-text{position:absolute;left:141px;top:377px;width:505px;font-size:16px;line-height:28.5px}
.btn{position:absolute;display:flex;align-items:center;justify-content:center;font-weight:700;font-size:15px;border-radius:4px;text-transform:uppercase}
.btn-red{left:139px;top:514px;width:145px;height:50px;background:var(--red)}
.btn-line{left:299px;top:514px;width:143px;height:50px;border:1.5px solid var(--red)}

/* contact strip */
.strip{top:703px;height:119px;background:var(--red)}
.strip-item{position:absolute;top:40px;font-size:16px;line-height:25px;white-space:nowrap}
.strip-item b{display:block;font-weight:700}

/* section arrow marker */
.marker{position:absolute;width:2px;background:var(--red)}
.pill{position:absolute;width:32px;height:46px;border:1.5px solid var(--red);border-radius:16px;display:flex;align-items:center;justify-content:center}
.pill.light{border-color:#ddd}

/* about */
.about{top:822px;height:551px;background:var(--black)}
.about-text{position:absolute;left:141px;top:1025px;width:448px;font-size:17px;line-height:37px}
.about-photo{position:absolute;left:668px;top:908px;width:387px;height:386px;background:linear-gradient(180deg,#d9d9d6 0%,#c4c4c0 45%,#3b3d44 60%,#2a2c33 100%)}
.next{position:absolute;left:1012px;top:1063px;width:76px;height:76px;border-radius:50%;background:var(--black);display:flex;align-items:center;justify-content:center}
.dots{position:absolute;left:826px;top:1263px;display:flex;gap:10px}
.dot{width:16px;height:16px;border-radius:50%;background:var(--white)}
.dot.on{background:var(--red)}

/* classes */
.classes{top:1373px;height:632px;background:var(--panel)}
.card{position:absolute;border-radius:8px;overflow:hidden}
.card-title{position:absolute;left:19px;top:34px;font-family:"Archivo",sans-serif;font-weight:800;font-size:28px;color:var(--white);white-space:nowrap}
.card-body{position:absolute;left:21px;bottom:34px;width:165px;font-size:16px;line-height:28px}
.card.active{border:3px solid var(--red)}

/* why */
.why{top:2005px;height:371px;background:linear-gradient(90deg,#b71c22 0%,#a8191e 40%,#c7292f 70%,#b81c22 100%)}
.video{position:absolute;left:139px;top:2079px;width:329px;height:221px;background:radial-gradient(ellipse 90px 80px at 164px 110px,#5a5a5a,#141414 80%)}
.why-text{position:absolute;left:589px;top:2153px;width:478px;font-size:16.5px;line-height:33.5px}

/* pricing */
.pricing{top:2376px;height:694px;background:var(--black)}
.sub{position:absolute;left:141px;font-size:16px;font-weight:500}
.plan{position:absolute;top:2600px;width:288px;height:374px;background:var(--card);border-radius:6px}
.plan.featured{background:var(--red)}
.plan-name{position:absolute;left:20px;top:39px;font-family:"Archivo",sans-serif;font-weight:700;font-size:26px;letter-spacing:.5px}
.plan-price{position:absolute;left:20px;top:100px;font-size:30px;font-weight:700}
.plan-price small{font-size:17px;font-weight:500}
.plan-rule{position:absolute;left:20px;right:20px;top:146px;height:1px;background:#555}
.plan.featured .plan-rule{background:rgba(255,255,255,.55)}
.feature{position:absolute;left:20px;display:flex;align-items:center;gap:16px;font-size:16px}
.plan-btn{position:absolute;left:20px;right:20px;top:317px;height:42px;background:var(--white);border-radius:4px;color:var(--black);font-weight:700;font-size:15px;display:flex;align-items:center;justify-content:center}

/* instructors */
.team{top:3070px;height:632px;background:var(--panel)}

/* blog */
.blog{top:3702px;height:845px;background:var(--black)}
.blog-intro{position:absolute;left:713px;top:3757px;width:345px;font-size:16.5px;line-height:33px}
.rule{position:absolute;height:1px;background:#555}
.post{position:absolute;top:3941px;width:294px;height:423px;background:var(--white);border-radius:8px;overflow:hidden;color:var(--black)}
.post-photo{height:209px}
.post-title{position:absolute;left:27px;top:244px;width:160px;font-size:17px;font-weight:600;line-height:27px}
.post-date{position:absolute;right:22px;top:249px;font-size:9px;color:var(--grey)}
.post-text{position:absolute;left:27px;top:306px;width:190px;font-size:13px;line-height:22px}
.post-more{position:absolute;left:27px;top:385px;display:flex;align-items:center;gap:18px;font-size:16px;font-weight:600;color:var(--red)}
.blog-btn{position:absolute;left:500px;top:4420px;width:202px;height:59px;border:1.5px solid #bbb;border-radius:5px;display:flex;align-items:center;justify-content:center;font-size:16px;font-weight:500}

/* footer */
.footer{top:4547px;height:296px;background:var(--panel)}
.foot-name{position:absolute;left:143px;top:4602px;font-size:16px;font-weight:700}
.foot-text{position:absolute;left:143px;top:4640px;width:350px;font-size:13px;line-height:26px}
.social{position:absolute;top:4745px;width:32px;height:32px;border:1.5px solid var(--white);border-radius:50%}
.links-title{position:absolute;left:888px;top:4602px;font-size:16px;font-weight:700}
.link{position:absolute;left:888px;font-size:13px}
</style>
</head>
<body>

<!-- hero -->
<section class="band hero">
  <div class="hero-photo" role="img" aria-label="Fighter in a knit cap and boxing gloves throwing a punch, black and white"></div>
</section>
<div class="logo"><div class="logo-mark"></div><div class="logo-name">Silver Heron Institute</div></div>
<nav class="nav">
  <a style="left:0">Home</a><a style="left:80px">Classes</a><a style="left:174px">Blogs</a><a style="left:250px">Schedule</a><a style="left:358px">Vides</a><a style="left:433px">About</a>
</nav>
<div class="hero-rule"></div>
<h1 class="hero-title"><span>TRAIN</span> YOUR<br>MARTIAL ARTS</h1>
<p class="hero-text">Lorem Ipsum is simply dummy text of the printing and typesetting industry. Lorem Ipsum has been the industry's standard dummy text ever since the 1500s,</p>
<div class="btn btn-red">Enroll now</div>
<div class="btn btn-line">Contact</div>

<!-- contact strip -->
<section class="band strip">
  <div class="strip-item" style="left:139px"><b>Email:</b>hello@silverheron.example</div>
  <div class="strip-item" style="left:519px"><b>Contact:</b>(0555) 0142 7788</div>
  <div class="strip-item" style="left:837px"><b>Address:</b>Heron Lane street no 12</div>
</section>

<!-- about -->
<section class="band about"></section>
<div class="pill" style="left:162px;top:833px"><svg width="12" height="16" viewBox="0 0 12 16"><path d="M6 1v13M1 9l5 5 5-5" fill="none" stroke="#e4222a" stroke-width="1.6"/></svg></div>
<h2 class="heading abs" style="left:142px;top:934px">About</h2>
<p class="about-text">Lorem Ipsum is simply dummy text of the printing and typesetting industry. Lorem Ipsum has been the industry's standard dummy text ever since the 1500s, Lorem Ipsum is simply dummy text of the printing and typesetting industry. Lorem Ipsum has been the industry's standard dummy text ever since the 1500s,</p>
<div class="about-photo" role="img" aria-label="Two jiu-jitsu students grappling on mats in a bright studio"></div>
<div class="next"><svg width="30" height="16" viewBox="0 0 30 16"><path d="M1 8h26M20 1l7 7-7 7" fill="none" stroke="#e4222a" stroke-width="2"/></svg></div>
<div class="dots"><div class="dot"></div><div class="dot on"></div><div class="dot"></div></div>

<!-- classes -->
<section class="band classes"></section>
<div class="marker" style="left:177px;top:1310px;height:48px"></div>
<div class="pill" style="left:162px;top:1358px"><svg width="12" height="16" viewBox="0 0 12 16"><path d="M6 1v13M1 9l5 5 5-5" fill="none" stroke="#e4222a" stroke-width="1.6"/></svg></div>
<h2 class="heading abs" style="left:142px;top:1434px">Our Classes</h2>

<div class="card" style="left:139px;top:1546px;width:211px;height:342px;background:linear-gradient(180deg,#9a9a9a,#5e5e5e 60%,#8a8a8a)" role="img" aria-label="Martial artist in black robes in a low stance">
  <div class="card-title">Jujitsu</div></div>
<div class="card active" style="left:372px;top:1543px;width:217px;height:348px;background:linear-gradient(180deg,#1a1a1a,#3b3a2c 50%,#151515)" role="img" aria-label="Fighter in a dark top holding a gym bag">
  <div class="card-title">combative</div>
  <div class="card-body">Lorem Ipsum is simply dummy text of the printing and</div></div>
<div class="card" style="left:611px;top:1546px;width:211px;height:342px;background:linear-gradient(180deg,#6b6b6b,#3a3a3a 55%,#1c1c1c)" role="img" aria-label="Boxer in gloves in a guard stance in a gym">
  <div class="card-title">Metaphysical</div></div>
<div class="card" style="left:846px;top:1546px;width:213px;height:342px;background:linear-gradient(180deg,#141414,#2c3446 55%,#121212)" role="img" aria-label="Athlete throwing a punch against a dark background">
  <div class="card-title">Motivation</div></div>

<!-- why choose us -->
<div class="marker" style="left:626px;top:1949px;height:46px;background:#ddd"></div>
<section class="band why" role="img" aria-label="Faint photo of a training class behind a red tint"></section>
<div class="pill light" style="left:611px;top:1995px"><svg width="12" height="16" viewBox="0 0 12 16"><path d="M6 1v13M1 9l5 5 5-5" fill="none" stroke="#fff" stroke-width="1.6"/></svg></div>
<div class="video" role="img" aria-label="Video thumbnail of a martial artist kneeling in a white gi">
  <svg class="abs" style="left:118px;top:78px" width="64" height="64" viewBox="0 0 64 64"><path d="M52 8L12 32l40 24z" fill="#fff"/></svg>
</div>
<h2 class="heading abs" style="left:583px;top:2077px;color:var(--white)">Why choose us</h2>
<p class="why-text">Lorem Ipsum is simply dummy text of the printing and typesetting industry. Lorem Ipsum has been the industry's standard dummy text ever since the 1500s, when an unknown printer took a galley of type and scrambled it to make a type specimen book.</p>

<!-- pricing -->
<section class="band pricing"></section>
<div class="marker" style="left:177px;top:2319px;height:41px;background:#ddd"></div>
<div class="pill light" style="left:162px;top:2366px"><svg width="12" height="16" viewBox="0 0 12 16"><path d="M6 1v13M1 9l5 5 5-5" fill="none" stroke="#fff" stroke-width="1.6"/></svg></div>
<h2 class="heading abs" style="left:142px;top:2446px">Our Pricing</h2>
<p class="sub" style="top:2505px">choose your level</p>

<div class="plan" style="left:139px">
  <div class="plan-name">BEGINNER</div>
  <div class="plan-price">$7<small>/month</small></div>
  <div class="plan-rule"></div>
  <div class="feature" style="top:178px"><svg width="28" height="28" viewBox="0 0 28 28"><circle cx="14" cy="14" r="12.5" fill="none" stroke="#ddd" stroke-width="1.4"/><path d="M8 14h11M15 10l4 4-4 4" fill="none" stroke="#ddd" stroke-width="1.4"/></svg><span>3 classes per week</span></div>
  <div class="feature" style="top:219px"><svg width="28" height="28" viewBox="0 0 28 28"><circle cx="14" cy="14" r="12.5" fill="none" stroke="#ddd" stroke-width="1.4"/><path d="M8 14h11M15 10l4 4-4 4" fill="none" stroke="#ddd" stroke-width="1.4"/></svg><span>3 classes per week</span></div>
  <div class="feature" style="top:260px"><svg width="28" height="28" viewBox="0 0 28 28"><circle cx="14" cy="14" r="12.5" fill="none" stroke="#ddd" stroke-width="1.4"/><path d="M8 14h11M15 10l4 4-4 4" fill="none" stroke="#ddd" stroke-width="1.4"/></svg><span>3 classes per week</span></div>
  <div class="plan-btn">ENROLL NOW</div>
</div>
<div class="plan featured" style="left:455px">
  <div class="plan-name">INTERMEDIATE</div>
  <div class="plan-price">$7<small>/month</small></div>
  <div class="plan-rule"></div>
  <div class="feature" style="top:178px"><svg width="28" height="28" viewBox="0 0 28 28"><circle cx="14" cy="14" r="12.5" fill="none" stroke="#fff" stroke-width="1.4"/><path d="M8 14h11M15 10l4 4-4 4" fill="none" stroke="#fff" stroke-width="1.4"/></svg><span>3 classes per week</span></div>
  <div class="feature" style="top:219px"><svg width="28" height="28" viewBox="0 0 28 28"><circle cx="14" cy="14" r="12.5" fill="none" stroke="#fff" stroke-width="1.4"/><path d="M8 14h11M15 10l4 4-4 4" fill="none" stroke="#fff" stroke-width="1.4"/></svg><span>3 classes per week</span></div>
  <div class="feature" style="top:260px"><svg width="28" height="28" viewBox="0 0 28 28"><circle cx="14" cy="14" r="12.5" fill="none" stroke="#fff" stroke-width="1.4"/><path d="M8 14h11M15 10l4 4-4 4" fill="none" stroke="#fff" stroke-width="1.4"/></svg><span>3 classes per week</span></div>
  <div class="plan-btn">ENROLL NOW</div>
</div>
<div class="plan" style="left:771px">
  <div class="plan-name">ADVANCED</div>
  <div class="plan-price">$7<small>/month</small></div>
  <div class="plan-rule"></div>
  <div class="feature" style="top:178px"><svg width="28" height="28" viewBox="0 0 28 28"><circle cx="14" cy="14" r="12.5" fill="none" stroke="#ddd" stroke-width="1.4"/><path d="M8 14h11M15 10l4 4-4 4" fill="none" stroke="#ddd" stroke-width="1.4"/></svg><span>3 classes per week</span></div>
  <div class="feature" style="top:219px"><svg width="28" height="28" viewBox="0 0 28 28"><circle cx="14" cy="14" r="12.5" fill="none" stroke="#ddd" stroke-width="1.4"/><path d="M8 14h11M15 10l4 4-4 4" fill="none" stroke="#ddd" stroke-width="1.4"/></svg><span>3 classes per week</span></div>
  <div class="feature" style="top:260px"><svg width="28" height="28" viewBox="0 0 28 28"><circle cx="14" cy="14" r="12.5" fill="none" stroke="#ddd" stroke-width="1.4"/><path d="M8 14h11M15 10l4 4-4 4" fill="none" stroke="#ddd" stroke-width="1.4"/></svg><span>3 classes per week</span></div>
  <div class="plan-btn">ENROLL NOW</div>
</div>

<!-- instructors -->
<section class="band team"></section>
<div class="marker" style="left:177px;top:3008px;height:42px"></div>
<div class="pill" style="left:162px;top:3053px"><svg width="12" height="16" viewBox="0 0 12 16"><path d="M6 1v13M1 9l5 5 5-5" fill="none" stroke="#e4222a" stroke-width="1.6"/></svg></div>
<h2 class="heading abs" style="left:142px;top:3133px">Our Instructor</h2>
<p class="sub" style="top:3184px">You will be trained by professionals</p>

<div class="card" style="left:139px;top:3241px;width:211px;height:344px;background:linear-gradient(180deg,#262626,#4a4636 50%,#1e1e1e)" role="img" aria-label="Instructor in a dark top seated in a boxing ring">
  <div class="card-title">Talon Marsh</div>
  <div class="card-body">Lorem Ipsum is simply dummy text of the printing and</div></div>
<div class="card" style="left:374px;top:3241px;width:212px;height:344px;background:linear-gradient(180deg,#1a2230,#2a3850 50%,#121822)" role="img" aria-label="Instructor in dark robes and a wide hat">
  <div class="card-title">Wrenley</div></div>
<div class="card" style="left:611px;top:3241px;width:211px;height:344px;background:linear-gradient(180deg,#3a3a3a,#8a8a8a 60%,#4a4a4a)" role="img" aria-label="Instructor in a white fencing jacket holding a mask">
  <div class="card-title">Corin Vale</div></div>
<div class="card" style="left:846px;top:3238px;width:213px;height:344px;background:linear-gradient(180deg,#2a3036,#44505a 55%,#1e2428)" role="img" aria-label="Instructor in a boxing stance with red gloves">
  <div class="card-title">Jessa Pike</div></div>

<!-- blog -->
<section class="band blog"></section>
<div class="marker" style="left:177px;top:3638px;height:40px"></div>
<div class="pill" style="left:162px;top:3680px"><svg width="12" height="16" viewBox="0 0 12 16"><path d="M6 1v13M1 9l5 5 5-5" fill="none" stroke="#e4222a" stroke-width="1.6"/></svg></div>
<h2 class="heading abs" style="left:139px;top:3763px">Our Instructor</h2>
<p class="blog-intro">Lorem Ipsum is simply dummy text of the printing and typesetting industry. Lorem Ipsum has been the industry's</p>
<div class="rule" style="left:139px;top:3884px;width:920px"></div>

<article class="post" style="left:139px">
  <div class="post-photo" role="img" aria-label="Martial artist in a kick pose on a beach at sunset" style="background:linear-gradient(180deg,#b9a089,#e0a257 45%,#6e4a2c 70%,#3a2a1e)"></div>
  <div class="post-title">Lorem ipsum is dummy text</div><div class="post-date">Aug 04 2022</div>
  <p class="post-text">Lorem Ipsum is simply dummy text of the printing and typesetting industry.</p>
  <div class="post-more">Read More <svg width="18" height="18" viewBox="0 0 18 18"><circle cx="9" cy="9" r="9" fill="#e4222a"/><path d="M5 9h7M9.5 6l3 3-3 3" fill="none" stroke="#fff" stroke-width="1.6"/></svg></div>
</article>
<article class="post" style="left:453px">
  <div class="post-photo" role="img" aria-label="Two boxers exchanging punches in a dark gym" style="background:linear-gradient(180deg,#1e1e1e,#4a3030 50%,#222)"></div>
  <div class="post-title">Lorem ipsum is dummy text</div><div class="post-date">Aug 04 2022</div>
  <p class="post-text">Lorem Ipsum is simply dummy text of the printing and typesetting industry.</p>
  <div class="post-more">Read More <svg width="18" height="18" viewBox="0 0 18 18"><circle cx="9" cy="9" r="9" fill="#e4222a"/><path d="M5 9h7M9.5 6l3 3-3 3" fill="none" stroke="#fff" stroke-width="1.6"/></svg></div>
</article>
<article class="post" style="left:766px">
  <div class="post-photo" role="img" aria-label="Two fighters grappling in a bright concrete room" style="background:linear-gradient(180deg,#d4d4d4,#a8a8a8 50%,#6c6c6c)"></div>
  <div class="post-title">Lorem ipsum is dummy text</div><div class="post-date">Aug 04 2022</div>
  <p class="post-text">Lorem Ipsum is simply dummy text of the printing and typesetting industry.</p>
  <div class="post-more">Read More <svg width="18" height="18" viewBox="0 0 18 18"><circle cx="9" cy="9" r="9" fill="#e4222a"/><path d="M5 9h7M9.5 6l3 3-3 3" fill="none" stroke="#fff" stroke-width="1.6"/></svg></div>
</article>

<div class="rule" style="left:139px;top:4449px;width:337px"></div>
<div class="rule" style="left:722px;top:4449px;width:337px"></div>
<div class="blog-btn">Go to Blog Page</div>

<!-- footer -->
<footer class="band footer"></footer>
<div class="foot-name">Silver Heron Institute</div>
<p class="foot-text">Lorem Ipsum is simply dummy text of the printing and typesetting industry. Lorem Ipsum has been the industry's</p>
<div class="social" style="left:139px" aria-label="Social link"></div>
<div class="social" style="left:187px" aria-label="Social link"></div>
<div class="social" style="left:234px" aria-label="Social link"></div>
<div class="links-title">Quick Links</div>
<div class="link" style="top:4640px">→ Home</div>
<div class="link" style="top:4672px">→ Courses</div>
<div class="link" style="top:4704px">→ Blog</div>
<div class="link" style="top:4736px">→ Contact</div>

</body>
</html>
```